A2 Desk calendar/planner *landscape*

We need a promotional a2 desk calendar for our customers (examples attached). Basically a marketing item so that our business is always fresh in the customer's mind sitting at their desk. It needs to be a2 Landscape as it will be a 20-page tear-off pad. Including logos, possibly images, 2020/21 calendar years, a big section in middle for writing on like examples. Business details and possibly a list of our industries and products. I have lots of images, logos and any other information visit www.brompellink.com.au to get an idea of what we do.
Industry/Entity Type
Hydraulic
Colors
Designer to choose colors to be used in the design.
Requirements
Must have
- Buisness logo, 2020 and 2021 calander year boxes like examples attached, colour themebluje and white possiby to go with the our logo. website adress phone number info. australian holiday dates . slogan "Industry chosen hose and fittings provider"
Nice to have
- public holiday dates from ; https://www.tollimark.com.au/law-compliance/laws-regulations/public-holidays

```html
<!DOCTYPE html>
<html lang="en">
<head>
<meta charset="utf-8">
<title>Brompell Hose and Fittings – Desk Planner 2020/21</title>
<link href="https://fonts.googleapis.com/css2?family=Roboto+Condensed:wght@400;700&family=Roboto:wght@400;700&display=swap" rel="stylesheet">
<style>
:root{
  --canvas:#e9ebee;
  --brand-blue:#1f4fa8;
  --deep-blue:#1d5ea8;
  --frame-light:#c9dcee;
  --pipe:#a9d3ee;
  --grid-fine:#e3ebf2;
  --grid-bold:#cfdbe6;
  --orange:#f07a1e;
  --yellow:#f6c21a;
  --ink:#3a3f47;
  --muted:#7c828b;
  --badge:#d5dce4;
  --cal-2020:#e3eef8;
  --cal-2021:#ececee;
  --year-2020:#9fc4e6;
  --year-2021:#a7a9ad;
  --gold:#c9a24a;
}
*{box-sizing:border-box;margin:0;padding:0}
html,body{width:1200px;height:1000px;overflow:hidden;background:var(--canvas)}
body{position:relative;font-family:"Roboto",sans-serif;color:var(--ink)}

.planner-sheet{position:absolute;left:20px;top:94px;width:1160px;height:812px;
  background:linear-gradient(100deg,var(--deep-blue) 0%,var(--deep-blue) 30%,var(--frame-light) 75%,#e8f0f8 100%);
  box-shadow:0 4px 18px rgba(0,0,0,.18)}
.planner-sheet::after{content:"";position:absolute;left:0;right:0;bottom:0;height:26px;
  background:linear-gradient(90deg,var(--deep-blue) 0%,var(--deep-blue) 60%,#9fc1e2 100%)}
.sheet-inner{position:absolute;left:24px;top:22px;width:1112px;height:764px;
  background:linear-gradient(180deg,#ffffff 0%,#f6f7f9 100%);overflow:hidden;z-index:1}

.hero-art{position:absolute;left:0;top:0;width:372px;height:764px}

.brand{position:absolute;left:392px;top:20px;display:flex;align-items:center;gap:10px}
.brand-dot{width:44px;height:44px;border-radius:50%;background:var(--brand-blue)}
.brand-name{font-family:"Roboto Condensed",sans-serif;font-weight:700;color:var(--brand-blue);
  font-size:22px;line-height:1.05;letter-spacing:.5px;text-transform:uppercase}
.slogan{position:absolute;left:697px;top:16px;font-family:"Roboto Condensed",sans-serif;font-weight:700;
  color:var(--brand-blue);font-size:25px;line-height:1.05}
.partner-badge{position:absolute;left:980px;top:18px;width:46px;height:46px;border-radius:6px;background:var(--badge)}

.contact-line{position:absolute;left:392px;top:86px;display:flex;gap:22px;align-items:center;
  font-family:"Roboto Condensed",sans-serif;font-size:17px;color:var(--ink);font-weight:700}
.contact-line span{display:flex;align-items:center;gap:6px}
.contact-line svg{flex:none}

.industries{position:absolute;left:392px;top:116px;width:710px;font-family:"Roboto Condensed",sans-serif;
  font-weight:700;color:var(--orange);font-size:18.5px;line-height:23px;text-transform:uppercase}

.notes-area{position:absolute;left:394px;top:180px;width:700px;height:290px}
.notes-grid{position:absolute;left:6px;top:6px;right:6px;bottom:6px;background-color:#fbfcfd;
  background-image:
   linear-gradient(var(--grid-bold) 1px,transparent 1px),
   linear-gradient(90deg,var(--grid-bold) 1px,transparent 1px),
   linear-gradient(var(--grid-fine) 1px,transparent 1px),
   linear-gradient(90deg,var(--grid-fine) 1px,transparent 1px);
  background-size:40px 40px,40px 40px,8px 8px,8px 8px}
.notes-frame{position:absolute;inset:0}

.year-block{position:absolute;left:392px;width:580px;display:flex;padding:3px 4px 3px 0;overflow:hidden}
.year-2020{top:482px;height:126px;background:var(--cal-2020)}
.year-2021{top:624px;height:126px;background:var(--cal-2021)}
.year-label{width:38px;display:flex;align-items:center;justify-content:center}
.year-label span{transform:rotate(-90deg);font-family:"Roboto Condensed",sans-serif;font-weight:700;font-size:34px;letter-spacing:1px}
.year-2020 .year-label span{color:var(--year-2020)}
.year-2021 .year-label span{color:var(--year-2021)}
.months{flex:1;display:grid;grid-template-columns:repeat(6,1fr);grid-template-rows:60px 60px;column-gap:6px}
.month{overflow:hidden}
.month h4{font-family:"Roboto Condensed",sans-serif;font-weight:700;font-size:8px;color:var(--brand-blue);text-align:right;line-height:9px}
.year-2021 .month h4{color:var(--muted)}
.days{display:grid;grid-template-columns:repeat(7,1fr);font-size:5.2px;line-height:6.2px;text-align:center}
.days b{font-weight:400;color:var(--muted)}
.days i{font-style:normal;color:var(--ink)}
.start-1 i:first-of-type{grid-column-start:1}
.start-2 i:first-of-type{grid-column-start:2}
.start-3 i:first-of-type{grid-column-start:3}
.start-4 i:first-of-type{grid-column-start:4}
.start-5 i:first-of-type{grid-column-start:5}
.start-6 i:first-of-type{grid-column-start:6}
.start-7 i:first-of-type{grid-column-start:7}

.holidays{position:absolute;left:984px;top:484px;width:120px}
.holidays h3{font-family:"Roboto Condensed",sans-serif;font-weight:700;color:var(--brand-blue);font-size:10px;margin-bottom:5px}
.holidays dl{font-size:6.2px;line-height:7.3px}
.holidays dt{font-weight:700;color:var(--ink)}
.holidays dd{color:var(--muted);margin-bottom:3px}
</style>
</head>
<body>
<main class="planner-sheet">
 <div class="sheet-inner">

  <svg class="hero-art" viewBox="0 0 372 764" role="img" aria-label="Photo collage: close-up of yellow hydraulic machinery with wrapped hoses, with three circular photos of braided hose assemblies, an industrial machine and an engine bay">
   <defs>
    <linearGradient id="heroFill" x1="0" y1="0" x2="0.4" y2="1">
     <stop offset="0" stop-color="#f2b62a"/><stop offset=".45" stop-color="#b58a2c"/><stop offset="1" stop-color="#2c3a34"/>
    </linearGradient>
    <radialGradient id="circleA" cx=".5" cy=".5" r=".6"><stop offset="0" stop-color="#c9ccd0"/><stop offset="1" stop-color="#6f747a"/></radialGradient>
    <radialGradient id="circleB" cx=".5" cy=".5" r=".6"><stop offset="0" stop-color="#e8c24a"/><stop offset="1" stop-color="#5d6a70"/></radialGradient>
    <radialGradient id="circleC" cx=".5" cy=".5" r=".6"><stop offset="0" stop-color="#a7adb3"/><stop offset="1" stop-color="#2e3338"/></radialGradient>
   </defs>
   <path d="M0 0 H372 C330 180 300 420 322 764 H0 Z" fill="var(--orange)"/>
   <path d="M0 0 H352 C306 180 280 420 300 764 H0 Z" fill="var(--yellow)"/>
   <path d="M0 0 H338 C290 180 262 420 280 764 H0 Z" fill="url(#heroFill)"/>
   <circle cx="256" cy="144" r="114" fill="url(#circleA)" stroke="var(--gold)" stroke-width="4"/>
   <circle cx="256" cy="385" r="114" fill="url(#circleB)" stroke="var(--gold)" stroke-width="4"/>
   <circle cx="256" cy="629" r="114" fill="url(#circleC)" stroke="var(--gold)" stroke-width="4"/>
  </svg>

  <div class="brand">
   <span class="brand-dot"></span>
   <span class="brand-name">Brompell<br>Hose and Fittings</span>
  </div>
  <h1 class="slogan">Industry Chosen Hose<br>and Fittings Provider</h1>
  <div class="partner-badge" aria-hidden="true"></div>

  <div class="contact-line">
   <span><svg width="16" height="16" viewBox="0 0 16 16" fill="none" stroke="var(--brand-blue)" stroke-width="1.3"><circle cx="8" cy="8" r="6.5"/><ellipse cx="8" cy="8" rx="3" ry="6.5"/><path d="M1.5 8h13M2.5 4.5h11M2.5 11.5h11"/></svg>www.brompellink.com.au</span>
   <span><svg width="11" height="18" viewBox="0 0 11 18" fill="none" stroke="var(--brand-blue)" stroke-width="1.3"><rect x="1" y="1" width="9" height="16" rx="1.5"/><path d="M4 14.5h3"/></svg>0400 555 218</span>
   <span><svg width="20" height="14" viewBox="0 0 20 14" fill="none" stroke="var(--brand-blue)" stroke-width="1.3"><rect x="1" y="1" width="18" height="12"/><path d="M1 1l9 7 9-7M1 13l6-5M19 13l-6-5"/></svg>email@brompellink.com.au</span>
  </div>

  <p class="industries">Food &amp; Beverage / Processing • Manufacturing • Earth Moving • Mining<br>Construction • Agriculture • Forestry • Transport • Automotive • Marine</p>

  <section class="notes-area" aria-label="Notes">
   <div class="notes-grid"></div>
   <svg class="notes-frame" viewBox="0 0 700 290" fill="none">
    <rect x="4" y="4" width="692" height="282" rx="10" stroke="var(--pipe)" stroke-width="5"/>
    <g stroke="#5a8fb8" stroke-width="2">
     <path d="M30 0v10M680 0v10M0 150h10M690 140h10M690 205h10M50 282v8M0 290h14"/>
    </g>
   </svg>
  </section>

  <section class="year-block year-2020" aria-label="Calendar 2020">
   <div class="year-label"><span>2020</span></div>
   <div class="months">
    <div class="month"><h4>January</h4><div class="days start-4"><b>S</b><b>M</b><b>T</b><b>W</b><b>T</b><b>F</b><b>S</b><i>1</i><i>2</i><i>3</i><i>4</i><i>5</i><i>6</i><i>7</i><i>8</i><i>9</i><i>10</i><i>11</i><i>12</i><i>13</i><i>14</i><i>15</i><i>16</i><i>17</i><i>18</i><i>19</i><i>20</i><i>21</i><i>22</i><i>23</i><i>24</i><i>25</i><i>26</i><i>27</i><i>28</i><i>29</i><i>30</i><i>31</i></div></div>
    <div class="month"><h4>February</h4><div class="days start-7"><b>S</b><b>M</b><b>T</b><b>W</b><b>T</b><b>F</b><b>S</b><i>1</i><i>2</i><i>3</i><i>4</i><i>5</i><i>6</i><i>7</i><i>8</i><i>9</i><i>10</i><i>11</i><i>12</i><i>13</i><i>14</i><i>15</i><i>16</i><i>17</i><i>18</i><i>19</i><i>20</i><i>21</i><i>22</i><i>23</i><i>24</i><i>25</i><i>26</i><i>27</i><i>28</i><i>29</i></div></div>
    <div class="month"><h4>March</h4><div class="days start-1"><b>S</b><b>M</b><b>T</b><b>W</b><b>T</b><b>F</b><b>S</b><i>1</i><i>2</i><i>3</i><i>4</i><i>5</i><i>6</i><i>7</i><i>8</i><i>9</i><i>10</i><i>11</i><i>12</i><i>13</i><i>14</i><i>15</i><i>16</i><i>17</i><i>18</i><i>19</i><i>20</i><i>21</i><i>22</i><i>23</i><i>24</i><i>25</i><i>26</i><i>27</i><i>28</i><i>29</i><i>30</i><i>31</i></div></div>
    <div class="month"><h4>April</h4><div class="days start-4"><b>S</b><b>M</b><b>T</b><b>W</b><b>T</b><b>F</b><b>S</b><i>1</i><i>2</i><i>3</i><i>4</i><i>5</i><i>6</i><i>7</i><i>8</i><i>9</i><i>10</i><i>11</i><i>12</i><i>13</i><i>14</i><i>15</i><i>16</i><i>17</i><i>18</i><i>19</i><i>20</i><i>21</i><i>22</i><i>23</i><i>24</i><i>25</i><i>26</i><i>27</i><i>28</i><i>29</i><i>30</i></div></div>
    <div class="month"><h4>May</h4><div class="days start-6"><b>S</b><b>M</b><b>T</b><b>W</b><b>T</b><b>F</b><b>S</b><i>1</i><i>2</i><i>3</i><i>4</i><i>5</i><i>6</i><i>7</i><i>8</i><i>9</i><i>10</i><i>11</i><i>12</i><i>13</i><i>14</i><i>15</i><i>16</i><i>17</i><i>18</i><i>19</i><i>20</i><i>21</i><i>22</i><i>23</i><i>24</i><i>25</i><i>26</i><i>27</i><i>28</i><i>29</i><i>30</i><i>31</i></div></div>
    <div class="month"><h4>June</h4><div class="days start-2"><b>S</b><b>M</b><b>T</b><b>W</b><b>T</b><b>F</b><b>S</b><i>1</i><i>2</i><i>3</i><i>4</i><i>5</i><i>6</i><i>7</i><i>8</i><i>9</i><i>10</i><i>11</i><i>12</i><i>13</i><i>14</i><i>15</i><i>16</i><i>17</i><i>18</i><i>19</i><i>20</i><i>21</i><i>22</i><i>23</i><i>24</i><i>25</i><i>26</i><i>27</i><i>28</i><i>29</i><i>30</i></div></div>
    <div class="month"><h4>July</h4><div class="days start-4"><b>S</b><b>M</b><b>T</b><b>W</b><b>T</b><b>F</b><b>S</b><i>1</i><i>2</i><i>3</i><i>4</i><i>5</i><i>6</i><i>7</i><i>8</i><i>9</i><i>10</i><i>11</i><i>12</i><i>13</i><i>14</i><i>15</i><i>16</i><i>17</i><i>18</i><i>19</i><i>20</i><i>21</i><i>22</i><i>23</i><i>24</i><i>25</i><i>26</i><i>27</i><i>28</i><i>29</i><i>30</i><i>31</i></div></div>
    <div class="month"><h4>August</h4><div class="days start-7"><b>S</b><b>M</b><b>T</b><b>W</b><b>T</b><b>F</b><b>S</b><i>1</i><i>2</i><i>3</i><i>4</i><i>5</i><i>6</i><i>7</i><i>8</i><i>9</i><i>10</i><i>11</i><i>12</i><i>13</i><i>14</i><i>15</i><i>16</i><i>17</i><i>18</i><i>19</i><i>20</i><i>21</i><i>22</i><i>23</i><i>24</i><i>25</i><i>26</i><i>27</i><i>28</i><i>29</i><i>30</i><i>31</i></div></div>
    <div class="month"><h4>September</h4><div class="days start-3"><b>S</b><b>M</b><b>T</b><b>W</b><b>T</b><b>F</b><b>S</b><i>1</i><i>2</i><i>3</i><i>4</i><i>5</i><i>6</i><i>7</i><i>8</i><i>9</i><i>10</i><i>11</i><i>12</i><i>13</i><i>14</i><i>15</i><i>16</i><i>17</i><i>18</i><i>19</i><i>20</i><i>21</i><i>22</i><i>23</i><i>24</i><i>25</i><i>26</i><i>27</i><i>28</i><i>29</i><i>30</i></div></div>
    <div class="month"><h4>October</h4><div class="days start-5"><b>S</b><b>M</b><b>T</b><b>W</b><b>T</b><b>F</b><b>S</b><i>1</i><i>2</i><i>3</i><i>4</i><i>5</i><i>6</i><i>7</i><i>8</i><i>9</i><i>10</i><i>11</i><i>12</i><i>13</i><i>14</i><i>15</i><i>16</i><i>17</i><i>18</i><i>19</i><i>20</i><i>21</i><i>22</i><i>23</i><i>24</i><i>25</i><i>26</i><i>27</i><i>28</i><i>29</i><i>30</i><i>31</i></div></div>
    <div class="month"><h4>November</h4><div class="days start-1"><b>S</b><b>M</b><b>T</b><b>W</b><b>T</b><b>F</b><b>S</b><i>1</i><i>2</i><i>3</i><i>4</i><i>5</i><i>6</i><i>7</i><i>8</i><i>9</i><i>10</i><i>11</i><i>12</i><i>13</i><i>14</i><i>15</i><i>16</i><i>17</i><i>18</i><i>19</i><i>20</i><i>21</i><i>22</i><i>23</i><i>24</i><i>25</i><i>26</i><i>27</i><i>28</i><i>29</i><i>30</i></div></div>
    <div class="month"><h4>December</h4><div class="days start-3"><b>S</b><b>M</b><b>T</b><b>W</b><b>T</b><b>F</b><b>S</b><i>1</i><i>2</i><i>3</i><i>4</i><i>5</i><i>6</i><i>7</i><i>8</i><i>9</i><i>10</i><i>11</i><i>12</i><i>13</i><i>14</i><i>15</i><i>16</i><i>17</i><i>18</i><i>19</i><i>20</i><i>21</i><i>22</i><i>23</i><i>24</i><i>25</i><i>26</i><i>27</i><i>28</i><i>29</i><i>30</i><i>31</i></div></div>
   </div>
  </section>

  <section class="year-block year-2021" aria-label="Calendar 2021">
   <div class="year-label"><span>2021</span></div>
   <div class="months">
    <div class="month"><h4>January</h4><div class="days start-6"><b>S</b><b>M</b><b>T</b><b>W</b><b>T</b><b>F</b><b>S</b><i>1</i><i>2</i><i>3</i><i>4</i><i>5</i><i>6</i><i>7</i><i>8</i><i>9</i><i>10</i><i>11</i><i>12</i><i>13</i><i>14</i><i>15</i><i>16</i><i>17</i><i>18</i><i>19</i><i>20</i><i>21</i><i>22</i><i>23</i><i>24</i><i>25</i><i>26</i><i>27</i><i>28</i><i>29</i><i>30</i><i>31</i></div></div>
    <div class="month"><h4>February</h4><div class="days start-2"><b>S</b><b>M</b><b>T</b><b>W</b><b>T</b><b>F</b><b>S</b><i>1</i><i>2</i><i>3</i><i>4</i><i>5</i><i>6</i><i>7</i><i>8</i><i>9</i><i>10</i><i>11</i><i>12</i><i>13</i><i>14</i><i>15</i><i>16</i><i>17</i><i>18</i><i>19</i><i>20</i><i>21</i><i>22</i><i>23</i><i>24</i><i>25</i><i>26</i><i>27</i><i>28</i></div></div>
    <div class="month"><h4>March</h4><div class="days start-2"><b>S</b><b>M</b><b>T</b><b>W</b><b>T</b><b>F</b><b>S</b><i>1</i><i>2</i><i>3</i><i>4</i><i>5</i><i>6</i><i>7</i><i>8</i><i>9</i><i>10</i><i>11</i><i>12</i><i>13</i><i>14</i><i>15</i><i>16</i><i>17</i><i>18</i><i>19</i><i>20</i><i>21</i><i>22</i><i>23</i><i>24</i><i>25</i><i>26</i><i>27</i><i>28</i><i>29</i><i>30</i><i>31</i></div></div>
    <div class="month"><h4>April</h4><div class="days start-5"><b>S</b><b>M</b><b>T</b><b>W</b><b>T</b><b>F</b><b>S</b><i>1</i><i>2</i><i>3</i><i>4</i><i>5</i><i>6</i><i>7</i><i>8</i><i>9</i><i>10</i><i>11</i><i>12</i><i>13</i><i>14</i><i>15</i><i>16</i><i>17</i><i>18</i><i>19</i><i>20</i><i>21</i><i>22</i><i>23</i><i>24</i><i>25</i><i>26</i><i>27</i><i>28</i><i>29</i><i>30</i></div></div>
    <div class="month"><h4>May</h4><div class="days start-7"><b>S</b><b>M</b><b>T</b><b>W</b><b>T</b><b>F</b><b>S</b><i>1</i><i>2</i><i>3</i><i>4</i><i>5</i><i>6</i><i>7</i><i>8</i><i>9</i><i>10</i><i>11</i><i>12</i><i>13</i><i>14</i><i>15</i><i>16</i><i>17</i><i>18</i><i>19</i><i>20</i><i>21</i><i>22</i><i>23</i><i>24</i><i>25</i><i>26</i><i>27</i><i>28</i><i>29</i><i>30</i><i>31</i></div></div>
    <div class="month"><h4>June</h4><div class="days start-3"><b>S</b><b>M</b><b>T</b><b>W</b><b>T</b><b>F</b><b>S</b><i>1</i><i>2</i><i>3</i><i>4</i><i>5</i><i>6</i><i>7</i><i>8</i><i>9</i><i>10</i><i>11</i><i>12</i><i>13</i><i>14</i><i>15</i><i>16</i><i>17</i><i>18</i><i>19</i><i>20</i><i>21</i><i>22</i><i>23</i><i>24</i><i>25</i><i>26</i><i>27</i><i>28</i><i>29</i><i>30</i></div></div>
    <div class="month"><h4>July</h4><div class="days start-5"><b>S</b><b>M</b><b>T</b><b>W</b><b>T</b><b>F</b><b>S</b><i>1</i><i>2</i><i>3</i><i>4</i><i>5</i><i>6</i><i>7</i><i>8</i><i>9</i><i>10</i><i>11</i><i>12</i><i>13</i><i>14</i><i>15</i><i>16</i><i>17</i><i>18</i><i>19</i><i>20</i><i>21</i><i>22</i><i>23</i><i>24</i><i>25</i><i>26</i><i>27</i><i>28</i><i>29</i><i>30</i><i>31</i></div></div>
    <div class="month"><h4>August</h4><div class="days start-1"><b>S</b><b>M</b><b>T</b><b>W</b><b>T</b><b>F</b><b>S</b><i>1</i><i>2</i><i>3</i><i>4</i><i>5</i><i>6</i><i>7</i><i>8</i><i>9</i><i>10</i><i>11</i><i>12</i><i>13</i><i>14</i><i>15</i><i>16</i><i>17</i><i>18</i><i>19</i><i>20</i><i>21</i><i>22</i><i>23</i><i>24</i><i>25</i><i>26</i><i>27</i><i>28</i><i>29</i><i>30</i><i>31</i></div></div>
    <div class="month"><h4>September</h4><div class="days start-4"><b>S</b><b>M</b><b>T</b><b>W</b><b>T</b><b>F</b><b>S</b><i>1</i><i>2</i><i>3</i><i>4</i><i>5</i><i>6</i><i>7</i><i>8</i><i>9</i><i>10</i><i>11</i><i>12</i><i>13</i><i>14</i><i>15</i><i>16</i><i>17</i><i>18</i><i>19</i><i>20</i><i>21</i><i>22</i><i>23</i><i>24</i><i>25</i><i>26</i><i>27</i><i>28</i><i>29</i><i>30</i></div></div>
    <div class="month"><h4>October</h4><div class="days start-6"><b>S</b><b>M</b><b>T</b><b>W</b><b>T</b><b>F</b><b>S</b><i>1</i><i>2</i><i>3</i><i>4</i><i>5</i><i>6</i><i>7</i><i>8</i><i>9</i><i>10</i><i>11</i><i>12</i><i>13</i><i>14</i><i>15</i><i>16</i><i>17</i><i>18</i><i>19</i><i>20</i><i>21</i><i>22</i><i>23</i><i>24</i><i>25</i><i>26</i><i>27</i><i>28</i><i>29</i><i>30</i><i>31</i></div></div>
    <div class="month"><h4>November</h4><div class="days start-2"><b>S</b><b>M</b><b>T</b><b>W</b><b>T</b><b>F</b><b>S</b><i>1</i><i>2</i><i>3</i><i>4</i><i>5</i><i>6</i><i>7</i><i>8</i><i>9</i><i>10</i><i>11</i><i>12</i><i>13</i><i>14</i><i>15</i><i>16</i><i>17</i><i>18</i><i>19</i><i>20</i><i>21</i><i>22</i><i>23</i><i>24</i><i>25</i><i>26</i><i>27</i><i>28</i><i>29</i><i>30</i></div></div>
    <div class="month"><h4>December</h4><div class="days start-4"><b>S</b><b>M</b><b>T</b><b>W</b><b>T</b><b>F</b><b>S</b><i>1</i><i>2</i><i>3</i><i>4</i><i>5</i><i>6</i><i>7</i><i>8</i><i>9</i><i>10</i><i>11</i><i>12</i><i>13</i><i>14</i><i>15</i><i>16</i><i>17</i><i>18</i><i>19</i><i>20</i><i>21</i><i>22</i><i>23</i><i>24</i><i>25</i><i>26</i><i>27</i><i>28</i><i>29</i><i>30</i><i>31</i></div></div>
   </div>
  </section>

  <aside class="holidays">
   <h3>PUBLIC HOLIDAY 2020</h3>
   <dl>
    <dt>New Year's Day</dt><dd>Wednesday 1 January</dd>
    <dt>Australia Day</dt><dd>Monday 27 January</dd>
    <dt>Canberra Day</dt><dd>Monday 9 March</dd>
    <dt>Good Friday</dt><dd>Friday 10 April</dd>
    <dt>Easter Saturday</dt><dd>Saturday 11 April</dd>
    <dt>Easter Sunday</dt><dd>Sunday 12 April</dd>
    <dt>Easter Monday</dt><dd>Monday 13 April</dd>
    <dt>ANZAC Day</dt><dd>Saturday 25 April</dd>
    <dt>Declared public holiday</dt><dd>Monday 27 April</dd>
    <dt>Reconciliation Day</dt><dd>Monday 1 June</dd>
    <dt>Queen's Birthday</dt><dd>Monday 8 June</dd>
    <dt>Labour Day</dt><dd>Monday 5 October</dd>
    <dt>Christmas Day</dt><dd>Friday 25 December</dd>
    <dt>Boxing Day</dt><dd>Saturday 26 December &amp; Monday 28 December</dd>
   </dl>
  </aside>

 </div>
</main>
</body>
</html>
```